Window cleaning company in need of leaflet design

Family run business requires leaflet design.
Our company uses water fed pole with pure water which is what the leaflet needs to emphasise on (include a background picture of a water fed pole cleaning a window.)

other services we offer which i would like to include are:
• facia/soffit cleaning.
• Conservatory cleans.
• Gutter clearing which is performed by a gutter vacuum pictures of gutters before and after clean are provided to every customer if they require.
• pressure washing

uploaded company logo to be included on leaflet.
number to include is 07942615380
email address is Tbglasswash@mailvento.com
would also like a facebook symbol included to show we are on social media.
Thank you

Font styles to use
Serif
Sans Serif

Colors
00a990
33a6d7
3276b5
3277b5
34a7d8
87cfc6
33b8a4
cfdfed
85acd3

Requirements
Must have
• We use traditional and water fed pole methods of cleaning. So those hard to reach or awkward to clean windows are not a problem. No need for ladders.

Our water fed pole system uses 100% pure water. This is water that has been de-ironised and de-mineralised to ensue it’s perfectly pure for a spot free finish.

• fully insured

• regular and reliable service
• one off cleans available

Call dean on 07942615380 for a free quote

```html
<!DOCTYPE html>
<html lang="en">
<head>
<meta charset="utf-8">
<title>Brightpane Cleaners – Leaflet</title>
<link rel="stylesheet" href="https://fonts.googleapis.com/css2?family=Barlow+Condensed:wght@300;400;700&family=Open+Sans:wght@400;600&display=swap">
<style>
  :root {
    --teal: #00a990;
    --panel-blue: #4775b8;
    --title-blue: #3f6db3;
    --deep-navy: #1e1450;
    --ink: #2a2a2a;
    --white: #ffffff;
    --page: #ececec;
  }
  * { margin: 0; padding: 0; box-sizing: border-box; }
  html, body { width: 1200px; height: 2323px; overflow: hidden; background: var(--page); }
  .canvas { position: relative; width: 1200px; height: 2323px; }
  .leaflet {
    position: absolute; left: 50px; top: 384px;
    width: 892px; height: 1260px;
    transform: scale(1.2332); transform-origin: top left;
    overflow: hidden; background: var(--white);
    box-shadow: 0 12px 30px rgba(0,0,0,.25);
    font-family: "Open Sans", sans-serif;
  }
  .leaflet svg.shapes { position: absolute; inset: 0; }
  .brand {
    position: absolute; left: 38px; top: 108px;
    font-family: "Open Sans", sans-serif; font-weight: 400;
    font-size: 30px; line-height: 1; color: var(--white); letter-spacing: 0.5px;
  }
  .headline {
    position: absolute; left: 37px; top: 175px;
    font-family: "Barlow Condensed", sans-serif; font-weight: 700;
    font-size: 60px; line-height: 62px; color: var(--white); text-transform: uppercase;
  }
  .services { position: absolute; left: 37px; top: 690px; width: 393px; }
  .services h2 {
    font-family: "Barlow Condensed", sans-serif; font-weight: 700;
    font-size: 54px; line-height: 1; color: var(--title-blue); margin-bottom: 22px;
  }
  .services ul { list-style: none; }
  .services li {
    position: relative; padding-left: 48px;
    font-size: 22.5px; line-height: 32.5px; color: var(--ink); margin-bottom: 9px;
  }
  .services li::before {
    content: ""; position: absolute; left: 1px; top: 7px;
    width: 19px; height: 19px; border-radius: 50%; background: var(--teal);
  }
  .services li::after {
    content: ""; position: absolute; left: 7px; top: 11px;
    width: 5px; height: 8px; border: solid var(--white); border-width: 0 2px 2px 0;
    transform: rotate(45deg);
  }
  .benefits { position: absolute; left: 488px; top: 768px; width: 372px; list-style: none; }
  .benefits li {
    position: relative; padding-left: 37px; color: var(--white);
    font-size: 16px; line-height: 22.5px;
  }
  .benefits li.para { margin-bottom: 14px; }
  .benefits li.short { margin-bottom: 6px; }
  .benefits li::before {
    content: ""; position: absolute; left: 4px; top: 2px;
    width: 7px; height: 14px; border: solid var(--white); border-width: 0 3px 3px 0;
    transform: rotate(40deg);
  }
  .quote-call {
    position: absolute; left: 36px; top: 1132px;
    font-family: "Barlow Condensed", sans-serif; font-weight: 300;
    font-size: 44px; line-height: 50px; color: var(--white); text-transform: uppercase;
  }
  .divider { position: absolute; left: 323px; top: 1138px; width: 3px; height: 113px; background: var(--teal); }
  .phone {
    position: absolute; left: 372px; top: 1118px;
    font-family: "Barlow Condensed", sans-serif; font-weight: 400;
    font-size: 86px; line-height: 1; color: var(--white);
  }
  .email {
    position: absolute; left: 373px; top: 1202px;
    font-size: 31px; line-height: 1.2; color: var(--white);
  }
  .social-square {
    position: absolute; left: 787px; top: 1132px;
    width: 60px; height: 60px; border-radius: 6px; background: var(--title-blue);
  }
</style>
</head>
<body>
<div class="canvas">
  <div class="leaflet">
    <svg class="shapes" viewBox="0 0 892 1260" width="892" height="1260">
      <defs>
        <linearGradient id="heroTone" x1="0" y1="0" x2="1" y2="0.4">
          <stop offset="0" stop-color="#2b3b6e"/>
          <stop offset="0.45" stop-color="#5a6c9c"/>
          <stop offset="0.75" stop-color="#2a3050"/>
          <stop offset="1" stop-color="#141a33"/>
        </linearGradient>
        <linearGradient id="bigCircleTone" x1="0" y1="0" x2="1" y2="1">
          <stop offset="0" stop-color="#d9d6cc"/>
          <stop offset="0.5" stop-color="#9ea3a0"/>
          <stop offset="1" stop-color="#8a7a5e"/>
        </linearGradient>
        <linearGradient id="smallCircleTone" x1="0" y1="0" x2="0" y2="1">
          <stop offset="0" stop-color="#b9c9b0"/>
          <stop offset="0.4" stop-color="#5f8a4a"/>
          <stop offset="1" stop-color="#3b6a32"/>
        </linearGradient>
      </defs>

      <rect class="hero-photo" x="0" y="0" width="892" height="720" fill="url(#heroTone)" role="img" aria-label="Photo of a cleaner using a water fed pole on a window"/>

      <rect class="benefit-panel" x="456" y="640" width="436" height="420" fill="var(--panel-blue)"/>

      <path class="teal-swoosh" d="M0,585 C120,520 260,555 340,615 C390,652 430,662 470,652 L470,668 C420,670 380,650 330,620 C250,568 110,545 0,610 Z" fill="var(--teal)"/>
      <path class="white-wave" d="M0,678 C100,585 250,600 330,650 C385,684 425,676 456,664 L456,1260 L0,1260 Z" fill="var(--white)"/>

      <circle cx="671" cy="500" r="245" fill="url(#bigCircleTone)" stroke="var(--teal)" stroke-width="8" role="img" aria-label="Close-up photo of a water fed pole brush cleaning glass"/>
      <circle cx="395" cy="563" r="120" fill="url(#smallCircleTone)" stroke="var(--teal)" stroke-width="8" role="img" aria-label="Photo of a pole brush with pure water running down a window"/>

      <path class="footer-wave" d="M0,1078 C140,1040 250,1118 380,1112 C520,1106 570,1060 700,1045 C800,1033 855,1012 892,1000 L892,1260 L0,1260 Z" fill="var(--deep-navy)"/>
    </svg>

    <div class="brand">Brightpane Cleaners</div>
    <h1 class="headline">Our company uses<br>water fed pole with<br>pure water</h1>

    <section class="services">
      <h2>SERVICES WE OFFER</h2>
      <ul>
        <li>Acia/soffit cleaning.</li>
        <li>Conservatory cleans.</li>
        <li>Gutter clearing which is performed by a gutter vacuum pictures of gutters before and after clean are provided to every customer if they require.</li>
        <li>Pressure washing</li>
      </ul>
    </section>

    <ul class="benefits">
      <li class="para">We use traditional and water fed pole methods of cleaning. So those hard to reach or awkward to clean windows are not a problem. No need for ladders.</li>
      <li class="para">Our water fed pole system uses 100% pure water. This is water that has been de-ironised and de-mineralised to ensue it’s perfectly pure for a spot free finish.</li>
      <li class="short">fully insured</li>
      <li class="short">regular and reliable service</li>
      <li class="short">one off cleans available</li>
    </ul>

    <div class="quote-call">Call Dean for<br>a free quote</div>
    <div class="divider"></div>
    <div class="phone">07942615380</div>
    <div class="email">Tbglasswash@mailvento.com</div>
    <div class="social-square"></div>
  </div>
</div>
</body>
</html>
```